A Student Forum developed (or Plugin tweaked) and installed on our current Wordpress Website

We require a Student Forum with LOGIN from our current Website.

Current website reference : www.harcombelearning.edu.au

The student forum is for students to ask questions about their studies and for ADMINS to reply.

The student forum should be able to cater for development of CATEGORIES. I have included a picture shot of the old forum in Joomla for understanding.

This job includes the overall design and also installation. It is perfectly fine, if the user sources a suitable Plugin as the basis of the forum, tweaks it to our branding and installs.

Please review the general look and feel of the website for branding.

Target Market(s)

Students

Industry/Entity Type

Education

Font styles to use
Sans Serif

Colors
ffffff

Requirements
Must have
• Categories in Forum - levels of administration
Nice to have
• uploads and downloads would be good
• place for student photo
• News etc.

```html
<!DOCTYPE html>
<html lang="en">
<head>
<meta charset="utf-8">
<title>Harcombe Learning Student Forum – Admin</title>
<link rel="stylesheet" href="https://fonts.googleapis.com/css2?family=Open+Sans:wght@400;600;700&display=swap">
<style>
:root{
  --navy:#243655;
  --page:#efefef;
  --white:#ffffff;
  --ink:#1d1d1d;
  --muted:#555;
  --line:#dcdcdc;
  --head:#dedede;
  --footer:#4e4e4e;
  --avatar:#9a8a7e;
}
*{box-sizing:border-box;margin:0;padding:0}
html,body{width:722px;height:1200px;overflow:hidden}
body{background:var(--page);font-family:"Open Sans",Arial,sans-serif;color:var(--ink);position:relative}
.topbar{position:absolute;top:0;left:0;width:722px;height:27px;background:var(--white);display:flex;justify-content:flex-end;align-items:center;padding-right:18px}
.topbar a{font-size:6.6px;color:var(--ink);text-decoration:none;padding:0 9px;height:27px;display:flex;align-items:center;gap:4px;border-left:1px solid #eee}
.topbar a:first-child{border-left:none}
.topbar svg{width:7px;height:7px;fill:var(--ink)}
.navbar{position:absolute;top:27px;left:0;width:722px;height:23px;background:var(--navy);display:flex;align-items:center;padding-left:146px}
.navbar a{font-size:6.6px;color:var(--white);text-decoration:none;padding:0 6px;height:23px;display:flex;align-items:center;border-right:1px solid rgba(255,255,255,.2)}
.navbar a:last-child{border-right:none}
.brand{position:absolute;top:0;left:69px;width:76px;height:69px;background:var(--white);box-shadow:0 1px 4px rgba(0,0,0,.25);display:flex;flex-direction:column;align-items:center;justify-content:center;gap:4px;z-index:2}
.brand-mark{width:18px;height:18px;background:var(--navy)}
.brand-name{font-size:7px;font-weight:700;color:var(--navy);text-align:center;line-height:1.2}
.toolbar{position:absolute;top:105px;left:95px;width:531px;height:21px}
.search{position:absolute;left:0;top:0;width:142px;height:21px;border:1px solid #cfcfcf;background:var(--page);font-size:5.5px;display:flex;align-items:center;padding-left:9px;gap:4px}
.search svg{width:5px;height:5px}
.select{position:absolute;top:0;height:21px;border:1px solid #cfcfcf;font-size:5.4px;display:flex;align-items:center;justify-content:space-between;padding:0 8px 0 9px}
.select::after{content:"";border:2px solid transparent;border-top:2.5px solid var(--ink);margin-top:2px}
.table-head{position:absolute;top:148px;left:96px;width:530px;height:22px;background:var(--head);border:1px solid #c6c6c6;display:flex;font-size:7px}
.table-head span{display:flex;align-items:center}
.th-topic{flex:1;padding-left:12px}
.th-num{width:54px;justify-content:center;border-left:1px solid #c6c6c6}
.th-posts{width:70px}
.topics{position:absolute;top:184px;left:96px;width:530px;display:flex;flex-direction:column;gap:8.4px}
.topic{height:77.6px;background:var(--white);box-shadow:0 1px 2px rgba(0,0,0,.12)}
.topic-main{height:57px;display:flex;align-items:center;border-bottom:1px solid #eee}
.avatar{width:26px;height:26px;border-radius:50%;background:linear-gradient(150deg,#c4b6a8,#5a5252);margin:0 11px 0 11px}
.topic-text{flex:1}
.topic-title{font-size:8px;font-weight:600}
.topic-alias{font-size:6.8px;color:var(--muted);margin-top:3px}
.count{width:54px;text-align:center;font-size:8.4px}
.count.posts{width:70px;margin-right:16px}
.topic-meta{height:20px;display:flex;align-items:center;padding:0 9px;font-size:5.6px;color:var(--muted)}
.topic-meta .sep{margin:0 5px}
.topic-meta .comment{display:flex;align-items:center;gap:3px}
.topic-meta .tools{margin-left:auto;display:flex;gap:10px}
.topic-meta svg{width:6px;height:6px;fill:#666}
.pager{position:absolute;top:1059px;right:97px;display:flex;align-items:center;gap:4px}
.pager .arrow{width:20px;height:9px;border-radius:5px;display:flex;align-items:center;justify-content:center}
.pager .prev{background:#a8a8a8;margin-right:6px}
.pager .next{background:var(--navy);margin-left:6px}
.pager .arrow svg{width:10px;height:5px;fill:var(--white)}
.pager .page{width:10px;height:10px;border:1px solid #999;border-radius:3px;font-size:5px;display:flex;align-items:center;justify-content:center}
.pager .gap{font-size:5px;width:9px;text-align:center}
.stats-bar{position:absolute;top:1102px;left:0;width:722px;height:19px;background:var(--navy);color:var(--white);font-size:8px;display:flex;align-items:center;gap:5px;padding-left:88px}
.stats-bar svg{width:9px;height:8px;fill:var(--white)}
.stats{position:absolute;top:1121px;left:0;width:722px;height:56px;background:var(--white);display:flex;padding:0 88px}
.stat{flex:1;display:flex;align-items:center;justify-content:center;gap:10px;border-right:1px solid #ddd;margin:10px 0}
.stat:last-child{border-right:none}
.stat svg{width:11px;height:10px;fill:var(--navy)}
.stat b{display:block;font-size:7.4px;color:var(--navy)}
.stat small{display:block;font-size:6.6px;color:var(--ink)}
.footer{position:absolute;top:1177px;left:0;width:722px;height:23px;background:var(--footer);color:#ddd;font-size:5.6px;display:flex;align-items:center;justify-content:center}
</style>
</head>
<body>

<header class="topbar">
  <a href="#"><svg viewBox="0 0 10 10"><path d="M5 1 0 5h1.5v4h2.5V6h2v3h2.5V5H10z"/></svg>Dashboard</a>
  <a href="#"><svg viewBox="0 0 10 10"><path d="M2 0h4l2 2v8H2z"/></svg>Forum Tools</a>
  <a href="#"><svg viewBox="0 0 10 10"><path d="M4 0h2v4h4v2H6v4H4V6H0V4h4z"/></svg>New Category</a>
  <a href="#"><svg viewBox="0 0 10 10"><path d="M0 2h5v1H1v6h6V6h1v4H0zM8 0l2 2-5 5H3V5z"/></svg>Edit</a>
  <a href="#"><svg viewBox="0 0 10 10"><path d="M0 5l1.5-1.5L4 6l4.5-4.5L10 3 4 9z"/></svg>Publish</a>
  <a href="#"><svg viewBox="0 0 10 10"><path d="M1.5 0 5 3.5 8.5 0 10 1.5 6.5 5 10 8.5 8.5 10 5 6.5 1.5 10 0 8.5 3.5 5 0 1.5z"/></svg>Unpublish</a>
  <a href="#"><svg viewBox="0 0 10 10"><path d="M1 1h8v1H1zM2 3h6v7H2zM4 0h2v1H4z"/></svg>Delete</a>
</header>

<nav class="navbar">
  <a href="#">Category Manager</a>
  <a href="#">User Manger</a>
  <a href="#">File Manager</a>
  <a href="#">Emoticon Manger</a>
  <a href="#">Rank Manager</a>
  <a href="#">Template Manager</a>
  <a href="#">Configutation</a>
  <a href="#">Plug in Manager</a>
  <a href="#">Trash Manager</a>
</nav>

<div class="brand">
  <div class="brand-mark"></div>
  <div class="brand-name">HARCOMBE<br>LEARNING</div>
</div>

<div class="toolbar">
  <div class="search"><svg viewBox="0 0 10 10"><circle cx="4" cy="4" r="3" fill="none" stroke="#1d1d1d" stroke-width="1.5"/><path d="M6 6l3.5 3.5" stroke="#1d1d1d" stroke-width="1.5"/></svg>SEARCH</div>
  <div class="select" style="left:349px;width:63px">REORDER</div>
  <div class="select" style="left:417px;width:65px">ASCENDING</div>
  <div class="select" style="left:488px;width:43px">20</div>
</div>

<div class="table-head">
  <span class="th-topic">Topic</span>
  <span class="th-num">Replies</span>
  <span class="th-num th-posts">Posts</span>
</div>

<main class="topics">
  <article class="topic"><div class="topic-main"><div class="avatar" role="img" aria-label="Member photo"></div><div class="topic-text"><div class="topic-title">Harcombe Student &nbsp;/ Trainer Discussion Board</div><div class="topic-alias">Alias :11-Harcombe student trainer discussion....</div></div><div class="count">5</div><div class="count posts">18</div></div><div class="topic-meta"><span>Updated 3 months ago</span><span class="sep">|</span><span>Marcus</span><span class="sep">|</span><span class="comment"><svg viewBox="0 0 10 10"><path d="M1 1h8v6H4L1 9V7H1z"/></svg>Comment</span><span class="tools"><svg viewBox="0 0 10 10"><path d="M5 0l1.5 3.3L10 3.7 7.4 6l.7 3.6L5 7.8 1.9 9.6 2.6 6 0 3.7l3.5-.4z"/></svg><svg viewBox="0 0 10 10"><path d="M2 4.5h6V10H2zM3 4.5V3a2 2 0 0 1 4 0v1.5H6V3a1 1 0 0 0-2 0v1.5z"/></svg><svg viewBox="0 0 10 10"><path d="M0 0h1v9h9v1H0zM2 5h1.5v3H2zM4.5 3H6v5H4.5zM7 4h1.5v4H7z"/></svg><svg viewBox="0 0 10 10"><path d="M0 3.5h2L7 1v8L2 6.5H0zM8 3.5h1.5v3H8zM2.5 6.5H4l1 3H3.5z"/></svg></span></div></article>

  <article class="topic"><div class="topic-main"><div class="avatar" role="img" aria-label="Member photo"></div><div class="topic-text"><div class="topic-title">Gold Coast Class May 2010</div><div class="topic-alias">Alias :11-Harcombe student trainer discussion....</div></div><div class="count">2</div><div class="count posts">45</div></div><div class="topic-meta"><span>Updated 3 months ago</span><span class="sep">|</span><span>Marcus</span><span class="sep">|</span><span class="comment"><svg viewBox="0 0 10 10"><path d="M1 1h8v6H4L1 9V7H1z"/></svg>Comment</span><span class="tools"><svg viewBox="0 0 10 10"><path d="M5 0l1.5 3.3L10 3.7 7.4 6l.7 3.6L5 7.8 1.9 9.6 2.6 6 0 3.7l3.5-.4z"/></svg><svg viewBox="0 0 10 10"><path d="M2 4.5h6V10H2zM3 4.5V3a2 2 0 0 1 4 0v1.5H6V3a1 1 0 0 0-2 0v1.5z"/></svg><svg viewBox="0 0 10 10"><path d="M0 0h1v9h9v1H0zM2 5h1.5v3H2zM4.5 3H6v5H4.5zM7 4h1.5v4H7z"/></svg><svg viewBox="0 0 10 10"><path d="M0 3.5h2L7 1v8L2 6.5H0zM8 3.5h1.5v3H8zM2.5 6.5H4l1 3H3.5z"/></svg></span></div></article>

  <article class="topic"><div class="topic-main"><div class="avatar" role="img" aria-label="Member photo"></div><div class="topic-text"><div class="topic-title">Reception Module Student / Trainer Discussion Board</div><div class="topic-alias">Alias :11-Harcombe student trainer discussion....</div></div><div class="count">1</div><div class="count posts">10</div></div><div class="topic-meta"><span>Updated 3 months ago</span><span class="sep">|</span><span>Marcus</span><span class="sep">|</span><span class="comment"><svg viewBox="0 0 10 10"><path d="M1 1h8v6H4L1 9V7H1z"/></svg>Comment</span><span class="tools"><svg viewBox="0 0 10 10"><path d="M5 0l1.5 3.3L10 3.7 7.4 6l.7 3.6L5 7.8 1.9 9.6 2.6 6 0 3.7l3.5-.4z"/></svg><svg viewBox="0 0 10 10"><path d="M2 4.5h6V10H2zM3 4.5V3a2 2 0 0 1 4 0v1.5H6V3a1 1 0 0 0-2 0v1.5z"/></svg><svg viewBox="0 0 10 10"><path d="M0 0h1v9h9v1H0zM2 5h1.5v3H2zM4.5 3H6v5H4.5zM7 4h1.5v4H7z"/></svg><svg viewBox="0 0 10 10"><path d="M0 3.5h2L7 1v8L2 6.5H0zM8 3.5h1.5v3H8zM2.5 6.5H4l1 3H3.5z"/></svg></span></div></article>

  <article class="topic"><div class="topic-main"><div class="avatar" role="img" aria-label="Member photo"></div><div class="topic-text"><div class="topic-title">Terminology Module</div><div class="topic-alias">Alias :11-Harcombe student trainer discussion....</div></div><div class="count">0</div><div class="count posts">1</div></div><div class="topic-meta"><span>Updated 3 months ago</span><span class="sep">|</span><span>Marcus</span><span class="sep">|</span><span class="comment"><svg viewBox="0 0 10 10"><path d="M1 1h8v6H4L1 9V7H1z"/></svg>Comment</span><span class="tools"><svg viewBox="0 0 10 10"><path d="M5 0l1.5 3.3L10 3.7 7.4 6l.7 3.6L5 7.8 1.9 9.6 2.6 6 0 3.7l3.5-.4z"/></svg><svg viewBox="0 0 10 10"><path d="M2 4.5h6V10H2zM3 4.5V3a2 2 0 0 1 4 0v1.5H6V3a1 1 0 0 0-2 0v1.5z"/></svg><svg viewBox="0 0 10 10"><path d="M0 0h1v9h9v1H0zM2 5h1.5v3H2zM4.5 3H6v5H4.5zM7 4h1.5v4H7z"/></svg><svg viewBox="0 0 10 10"><path d="M0 3.5h2L7 1v8L2 6.5H0zM8 3.5h1.5v3H8zM2.5 6.5H4l1 3H3.5z"/></svg></span></div></article>

  <article class="topic"><div class="topic-main"><div class="avatar" role="img" aria-label="Member photo"></div><div class="topic-text"><div class="topic-title">Medical Computing Module</div><div class="topic-alias">Alias :11-Harcombe student trainer discussion....</div></div><div class="count">5</div><div class="count posts">15</div></div><div class="topic-meta"><span>Updated 3 months ago</span><span class="sep">|</span><span>Marcus</span><span class="sep">|</span><span class="comment"><svg viewBox="0 0 10 10"><path d="M1 1h8v6H4L1 9V7H1z"/></svg>Comment</span><span class="tools"><svg viewBox="0 0 10 10"><path d="M5 0l1.5 3.3L10 3.7 7.4 6l.7 3.6L5 7.8 1.9 9.6 2.6 6 0 3.7l3.5-.4z"/></svg><svg viewBox="0 0 10 10"><path d="M2 4.5h6V10H2zM3 4.5V3a2 2 0 0 1 4 0v1.5H6V3a1 1 0 0 0-2 0v1.5z"/></svg><svg viewBox="0 0 10 10"><path d="M0 0h1v9h9v1H0zM2 5h1.5v3H2zM4.5 3H6v5H4.5zM7 4h1.5v4H7z"/></svg><svg viewBox="0 0 10 10"><path d="M0 3.5h2L7 1v8L2 6.5H0zM8 3.5h1.5v3H8zM2.5 6.5H4l1 3H3.5z"/></svg></span></div></article>

  <article class="topic"><div class="topic-main"><div class="avatar" role="img" aria-label="Member photo"></div><div class="topic-text"><div class="topic-title">Student Feedback and Job News</div><div class="topic-alias">Alias :11-Harcombe student trainer discussion....</div></div><div class="count">5</div><div class="count posts">18</div></div><div class="topic-meta"><span>Updated 3 months ago</span><span class="sep">|</span><span>Marcus</span><span class="sep">|</span><span class="comment"><svg viewBox="0 0 10 10"><path d="M1 1h8v6H4L1 9V7H1z"/></svg>Comment</span><span class="tools"><svg viewBox="0 0 10 10"><path d="M5 0l1.5 3.3L10 3.7 7.4 6l.7 3.6L5 7.8 1.9 9.6 2.6 6 0 3.7l3.5-.4z"/></svg><svg viewBox="0 0 10 10"><path d="M2 4.5h6V10H2zM3 4.5V3a2 2 0 0 1 4 0v1.5H6V3a1 1 0 0 0-2 0v1.5z"/></svg><svg viewBox="0 0 10 10"><path d="M0 0h1v9h9v1H0zM2 5h1.5v3H2zM4.5 3H6v5H4.5zM7 4h1.5v4H7z"/></svg><svg viewBox="0 0 10 10"><path d="M0 3.5h2L7 1v8L2 6.5H0zM8 3.5h1.5v3H8zM2.5 6.5H4l1 3H3.5z"/></svg></span></div></article>

  <article class="topic"><div class="topic-main"><div class="avatar" role="img" aria-label="Member photo"></div><div class="topic-text"><div class="topic-title">Medical Computing Module</div><div class="topic-alias">Alias :11-Harcombe student trainer discussion....</div></div><div class="count">5</div><div class="count posts">18</div></div><div class="topic-meta"><span>Updated 3 months ago</span><span class="sep">|</span><span>Marcus</span><span class="sep">|</span><span class="comment"><svg viewBox="0 0 10 10"><path d="M1 1h8v6H4L1 9V7H1z"/></svg>Comment</span><span class="tools"><svg viewBox="0 0 10 10"><path d="M5 0l1.5 3.3L10 3.7 7.4 6l.7 3.6L5 7.8 1.9 9.6 2.6 6 0 3.7l3.5-.4z"/></svg><svg viewBox="0 0 10 10"><path d="M2 4.5h6V10H2zM3 4.5V3a2 2 0 0 1 4 0v1.5H6V3a1 1 0 0 0-2 0v1.5z"/></svg><svg viewBox="0 0 10 10"><path d="M0 0h1v9h9v1H0zM2 5h1.5v3H2zM4.5 3H6v5H4.5zM7 4h1.5v4H7z"/></svg><svg viewBox="0 0 10 10"><path d="M0 3.5h2L7 1v8L2 6.5H0zM8 3.5h1.5v3H8zM2.5 6.5H4l1 3H3.5z"/></svg></span></div></article>

  <article class="topic"><div class="topic-main"><div class="avatar" role="img" aria-label="Member photo"></div><div class="topic-text"><div class="topic-title">Student Feedback and Job News</div><div class="topic-alias">Alias :11-Harcombe student trainer discussion....</div></div><div class="count">5</div><div class="count posts">18</div></div><div class="topic-meta"><span>Updated 3 months ago</span><span class="sep">|</span><span>Marcus</span><span class="sep">|</span><span class="comment"><svg viewBox="0 0 10 10"><path d="M1 1h8v6H4L1 9V7H1z"/></svg>Comment</span><span class="tools"><svg viewBox="0 0 10 10"><path d="M5 0l1.5 3.3L10 3.7 7.4 6l.7 3.6L5 7.8 1.9 9.6 2.6 6 0 3.7l3.5-.4z"/></svg><svg viewBox="0 0 10 10"><path d="M2 4.5h6V10H2zM3 4.5V3a2 2 0 0 1 4 0v1.5H6V3a1 1 0 0 0-2 0v1.5z"/></svg><svg viewBox="0 0 10 10"><path d="M0 0h1v9h9v1H0zM2 5h1.5v3H2zM4.5 3H6v5H4.5zM7 4h1.5v4H7z"/></svg><svg viewBox="0 0 10 10"><path d="M0 3.5h2L7 1v8L2 6.5H0zM8 3.5h1.5v3H8zM2.5 6.5H4l1 3H3.5z"/></svg></span></div></article>

  <article class="topic"><div class="topic-main"><div class="avatar" role="img" aria-label="Member photo"></div><div class="topic-text"><div class="topic-title">Medical Computing Module</div><div class="topic-alias">Alias :11-Harcombe student trainer discussion....</div></div><div class="count">5</div><div class="count posts">18</div></div><div class="topic-meta"><span>Updated 3 months ago</span><span class="sep">|</span><span>Marcus</span><span class="sep">|</span><span class="comment"><svg viewBox="0 0 10 10"><path d="M1 1h8v6H4L1 9V7H1z"/></svg>Comment</span><span class="tools"><svg viewBox="0 0 10 10"><path d="M5 0l1.5 3.3L10 3.7 7.4 6l.7 3.6L5 7.8 1.9 9.6 2.6 6 0 3.7l3.5-.4z"/></svg><svg viewBox="0 0 10 10"><path d="M2 4.5h6V10H2zM3 4.5V3a2 2 0 0 1 4 0v1.5H6V3a1 1 0 0 0-2 0v1.5z"/></svg><svg viewBox="0 0 10 10"><path d="M0 0h1v9h9v1H0zM2 5h1.5v3H2zM4.5 3H6v5H4.5zM7 4h1.5v4H7z"/></svg><svg viewBox="0 0 10 10"><path d="M0 3.5h2L7 1v8L2 6.5H0zM8 3.5h1.5v3H8zM2.5 6.5H4l1 3H3.5z"/></svg></span></div></article>

  <article class="topic"><div class="topic-main"><div class="avatar" role="img" aria-label="Member photo"></div><div class="topic-text"><div class="topic-title">Terminology Module</div><div class="topic-alias">Alias :11-Harcombe student trainer discussion....</div></div><div class="count">0</div><div class="count posts">1</div></div><div class="topic-meta"><span>Updated 3 months ago</span><span class="sep">|</span><span>Marcus</span><span class="sep">|</span><span class="comment"><svg viewBox="0 0 10 10"><path d="M1 1h8v6H4L1 9V7H1z"/></svg>Comment</span><span class="tools"><svg viewBox="0 0 10 10"><path d="M5 0l1.5 3.3L10 3.7 7.4 6l.7 3.6L5 7.8 1.9 9.6 2.6 6 0 3.7l3.5-.4z"/></svg><svg viewBox="0 0 10 10"><path d="M2 4.5h6V10H2zM3 4.5V3a2 2 0 0 1 4 0v1.5H6V3a1 1 0 0 0-2 0v1.5z"/></svg><svg viewBox="0 0 10 10"><path d="M0 0h1v9h9v1H0zM2 5h1.5v3H2zM4.5 3H6v5H4.5zM7 4h1.5v4H7z"/></svg><svg viewBox="0 0 10 10"><path d="M0 3.5h2L7 1v8L2 6.5H0zM8 3.5h1.5v3H8zM2.5 6.5H4l1 3H3.5z"/></svg></span></div></article>
</main>

<nav class="pager">
  <span class="arrow prev"><svg viewBox="0 0 10 5"><path d="M0 2.5 3 0v2h7v1H3v2z"/></svg></span>
  <span class="page">1</span><span class="page">2</span><span class="page">3</span><span class="page">4</span>
  <span class="gap">....</span>
  <span class="page">25</span>
  <span class="arrow next"><svg viewBox="0 0 10 5"><path d="M10 2.5 7 0v2H0v1h7v2z"/></svg></span>
</nav>

<div class="stats-bar"><svg viewBox="0 0 10 10"><path d="M0 0h1v9h9v1H0zM2 5h1.5v3H2zM4.5 3H6v5H4.5zM7 4h1.5v4H7z"/></svg>STATISTICS</div>
<section class="stats">
  <div class="stat"><svg viewBox="0 0 10 10"><path d="M0 1h2v2H0zM3 1h7v2H3zM0 4h2v2H0zM3 4h7v2H3zM0 7h2v2H0zM3 7h7v2H3z"/></svg><div><b>749</b><small>Topics</small></div></div>
  <div class="stat"><svg viewBox="0 0 10 10"><path d="M2 0h4l2.5 2.5V10H2z"/></svg><div><b>3698</b><small>Posts</small></div></div>
  <div class="stat"><svg viewBox="0 0 10 10"><path d="M0 5Q5-1 10 5 5 11 0 5zM5 3a2 2 0 1 0 0 4 2 2 0 0 0 0-4z"/></svg><div><b>2458972</b><small>Views</small></div></div>
  <div class="stat"><svg viewBox="0 0 10 10"><circle cx="5" cy="3" r="2"/><path d="M1.5 9a3.5 3 0 0 1 7 0z"/><circle cx="1.5" cy="4" r="1.3"/><circle cx="8.5" cy="4" r="1.3"/></svg><div><b>2587</b><small>Users</small></div></div>
  <div class="stat"><svg viewBox="0 0 10 10"><path d="M0 1h10v6H0zM1 2v4h8V2zM3 8h4v1H3z"/></svg><div><b>8</b><small>Online</small></div></div>
</section>

<footer class="footer">Copyrights @ 2018 All Rights Reserved</footer>

</body>
</html>
```